Amber Ridge Ventures, LLC Business Card

We need a logo that will be embossed or printed in a singular light color for Business Cards. Would be interested in seeing a Cypress Tree graphic. Our company name is Amber Ridge Ventures, LLC. Business Card layout and graphic should project imagine of confidence, integrity and strength.

```html
<!DOCTYPE html>
<html lang="en">
<head>
<meta charset="utf-8">
<title>Amber Ridge Ventures, LLC — Business Card</title>
<link rel="stylesheet" href="https://fonts.googleapis.com/css2?family=Cinzel:wght@400;600&family=Open+Sans:wght@400&display=swap">
<style>
  :root {
    --backdrop: #ece8e0;
    --card-white: #ffffff;
    --card-grey: #b9b9b9;
    --ink: #0b0b0b;
    --accent: #5b1d26;
    --silver: #a9a9a9;
    --paper-text: #f2f2f2;
  }
  * { margin: 0; padding: 0; box-sizing: border-box; }
  html, body { width: 1200px; height: 800px; overflow: hidden; }
  body {
    background: var(--backdrop);
    position: relative;
    font-family: "Open Sans", Arial, sans-serif;
  }
  .card {
    position: absolute;
    top: 257px;
    width: 500px;
    height: 286px;
    border-radius: 28px;
    overflow: hidden;
    box-shadow: 0 8px 22px rgba(0,0,0,0.18);
  }
  /* Front */
  .card-front {
    left: 60px;
    background: linear-gradient(180deg, var(--card-white) 0%, var(--card-white) 30%, var(--card-grey) 76%);
  }
  .card-front .ground-band {
    position: absolute;
    left: 0; right: 0; bottom: 0;
    height: 72px;
    background: var(--ink);
  }
  .card-front .company-name {
    position: absolute;
    top: 30px;
    right: 30px;
    font-family: "Cinzel", "Times New Roman", serif;
    font-weight: 400;
    font-size: 27px;
    letter-spacing: 0.5px;
    color: var(--ink);
    white-space: nowrap;
  }
  .card-front .brand-mark {
    position: absolute;
    left: 34px;
    top: 150px;
    width: 170px;
    text-align: center;
    font-family: "Cinzel", "Times New Roman", serif;
    font-weight: 600;
    font-size: 22px;
    line-height: 1.05;
    color: var(--ink);
  }
  .card-front .divider {
    position: absolute;
    left: 240px;
    top: 118px;
    width: 2px;
    height: 88px;
    background: var(--ink);
  }
  .contact-list {
    position: absolute;
    left: 254px;
    top: 118px;
    list-style: none;
  }
  .contact-list li {
    display: flex;
    align-items: center;
    gap: 7px;
    height: 22px;
    font-size: 12.5px;
    color: #1b1b1b;
  }
  .contact-list svg { width: 13px; height: 13px; flex: none; }
  .contact-list .plain-square {
    width: 11px; height: 11px; background: var(--accent); flex: none; margin: 0 1px;
  }
  .contact-list .plain-circle {
    width: 12px; height: 12px; border-radius: 50%; background: var(--accent); flex: none; margin: 0 0.5px;
  }
  /* Back */
  .card-back {
    left: 640px;
    background: var(--ink);
  }
  .card-back .brand-mark {
    position: absolute;
    left: 0; right: 0;
    top: 92px;
    text-align: center;
    font-family: "Cinzel", "Times New Roman", serif;
    font-weight: 600;
    font-size: 28px;
    line-height: 1.1;
    color: var(--silver);
  }
  .card-back .tagline {
    position: absolute;
    left: 0; right: 0;
    top: 178px;
    text-align: center;
    font-family: "Cinzel", "Times New Roman", serif;
    font-size: 12px;
    letter-spacing: 0.5px;
    color: var(--paper-text);
  }
  .card-back .website {
    position: absolute;
    left: 0; right: 0;
    bottom: 16px;
    text-align: center;
    font-size: 9.5px;
    color: var(--paper-text);
  }
</style>
</head>
<body>
  <section class="card card-front" aria-label="Card front">
    <div class="ground-band"></div>
    <h1 class="company-name">Amber Ridge Ventures, LLC</h1>
    <div class="brand-mark">Amber<br>Ridge</div>
    <div class="divider"></div>
    <ul class="contact-list">
      <li>
        <svg viewBox="0 0 16 16" aria-hidden="true"><path fill="var(--accent)" d="M3.6 1.2l2.3 2.7-1.3 1.7c.8 2 2.1 3.4 4.1 4.3l1.7-1.3 2.7 2.3-1.4 2.2C6.4 13 2.9 9.5 1.3 4.2z"/></svg>
        555-014-2276
      </li>
      <li>
        <svg viewBox="0 0 16 16" aria-hidden="true"><rect x="1.5" y="3.5" width="13" height="9" fill="none" stroke="var(--accent)" stroke-width="1.4"/><path d="M1.5 3.5L8 9l6.5-5.5" fill="none" stroke="var(--accent)" stroke-width="1.4"/></svg>
        info@amberridgeventures.com
      </li>
      <li><span class="plain-square"></span>AmberRidgeVenturesGroup</li>
      <li><span class="plain-circle"></span>@Amber_Ridge</li>
    </ul>
  </section>

  <section class="card card-back" aria-label="Card back">
    <div class="brand-mark">Amber Ridge<br>Ventures</div>
    <p class="tagline">STEADY ROOTS AND CLEAR VIEWS</p>
    <p class="website">www.amberridgeventures.com</p>
  </section>
</body>
</html>
```